Relaunch / Responsives, modernes Webdesign für ein Campingportal
Zielgruppe
Die zeltfuchs GmbH betreibt mit der Plattform www.zeltfuchs.de eines der führenden Campingportale in Deutschland.
Im Zuge des Relaunches soll ein frisches, neues und modernes Design der Webseite erfolgen und auch die mobile Nutzbarkeit durch ein responsives Design verbessert werden.
Zielgruppe sind Camperinnen und Camper bzw. solche, die es vielleicht einmal werden wollen. Ebenso natürlich auch die Betreiber der Campingplätze, die Mitglied bei zeltfuchs sein können und damit bei der Suche, auf der Karte und in den Regionen gefunden werden. Sie sind dann mit einer eigenen Campingplatzseite vertreten, auf der neben allen wichtigen Informationen auch Bilder und Videos vom Platz zu sehen sind.
Aktuell ist im Fokus ein Campingführer (Campingplatzsuche), der wie beschrieben auch per Karte erfolgt und mit Filtern eingeschränkt werden kann. Auch ein Blog ist vorhanden, es wird noch ein Forum geben usw.
Später wird auch noch ein Shop, etc. hinzukommen...
Aufgabenstellung
Das Design soll frisch, modern und natürlich responsiv sein. Das Logo ist dabei weiterhin gesetzt. Daran können Sie also z.B. die Farbgebung übernehmen (v.a. das Grün).
Das Design soll sich nicht mehr rein vertikal ausrichten (wie bisher) sondern horizontal über den gesamten Bildschirm.
Dabei muss z.B. auf der Startseite u.a. auch ein Feld vorhanden sein, in dem man Länder, Regionen oder direkt Campingplätze suchen kann uns sich ein Auswahlfeld mit den vorgeschlagenen Ergebnissen öffnet. So wie bei Hotelportalen zumeist auch.
Es gibt aktuell nachfolgende Seitentypen:
1. Startseite (bisher http://www.zeltfuchs.de/)
Hier soll u.a. auch ein Feld zur Eingabe eines Landes, einer Region oder eines Platzes existieren, bei dem bei Eingabe Auswahlmöglichkeiten sichtbar werden (wie bei Reiseportalen).
So z.B. bei:
Urlaubsquartier[Punkt]de
Stubo Nahweg
Tripbewerter
Auch eine Karte von Europa wäre hier ggf. interessant, die man dann beim Anklicken auf Deutschland fokussiert, danach dann weiter auf die Nordsee usw.
Zudem Flächen wo man besondere Themen oder Regionen noch einmal extra anführt "Campingplätze am Meer", "Campingplätze in den Bergen", "Campingplätze Stadtnah, usw.
Hier zum Beispiel dann auch später eine Grafik zum Shop usw.
Auch kann es einige Flächen geben, die man an Campingplätze vermieten kann, um auf der Startseite präsent zu sein. Also quasi einige exklusive Campingplätze.
Zudem sollte man einen Block haben, wo man besonders nachgefragte Regionenlinks vorstellen kann (Beliebte Reiseziele, Nordseeküste, Alpen, etc.).
Dies müssen aber keine Bilder sein, sondern können auch nur Links sein als Gruppe in einem Block.
Zudem muss es unten ein Textfeld geben, da es sonst schwer wird mit der Regionenseite bei Suchraum weiterhin gut zu ranken.
Selbstverständlich müssen auch Werbeflächen eingeplant sein für Suchraum adse..

```html
<!DOCTYPE html>
<html lang="de">
<head>
<meta charset="utf-8">
<title>zeltfuchs – Campingplatz Elbauen Strand</title>
<link href="https://fonts.googleapis.com/css2?family=Roboto:wght@300;400;500;700&display=swap" rel="stylesheet">
<style>
:root{
  --green:#8dc21f;
  --green-dark:#3c9a07;
  --navy:#0d2c6c;
  --ink:#1f1f1f;
  --text:#2b2b2b;
  --muted:#8a8a8a;
  --line:#e3e3e3;
  --footer:#f1f1f1;
}
*{margin:0;padding:0;box-sizing:border-box}
html,body{width:1200px;height:3482px;overflow:hidden;background:#fff}
body{font-family:'Roboto',sans-serif;color:var(--text);position:relative}
.abs{position:absolute}

/* header */
.site-header{position:absolute;left:0;top:0;width:1200px;height:78px;background:#fff}
.brand{position:absolute;display:flex;align-items:center;gap:10px;font-weight:700;color:var(--navy)}
.brand .mark{width:26px;height:26px;background:var(--green)}
.site-header .brand{left:86px;top:22px;font-size:28px}
.nav-item{position:absolute;top:14px;transform:translateX(-50%);display:flex;flex-direction:column;align-items:center;font-size:15px;color:#222}
.nav-item svg{width:30px;height:30px;margin-bottom:5px}
.nav-item.active{color:var(--green);font-weight:500}

.search-band{position:absolute;left:0;top:78px;width:1200px;height:99px;background:var(--navy)}
.search-field{position:absolute;left:273px;top:40px;width:558px;height:32px;background:#fff;border:2px solid var(--green);display:flex;align-items:center;padding-left:36px;font-size:15px;color:#222}
.search-field svg{position:absolute;left:5px;top:-8px;width:24px;height:34px}
.search-btn{position:absolute;left:839px;top:40px;width:90px;height:32px;background:var(--green);color:#fff;font-size:15px;display:flex;align-items:center;justify-content:center}

/* sidebar */
.sidebar{position:absolute;left:32px;top:207px;width:299px;height:1181px;border:1px solid #eee}
.sidebar .title{position:absolute;left:14px;top:17px;font-size:18px;font-weight:700;color:var(--ink)}
.sidebar .group{position:absolute;left:14px;width:268px;font-size:18px;font-weight:700;color:var(--ink);border-bottom:2px solid var(--green);padding-bottom:5px}
.sidebar ul{position:absolute;list-style:none;font-size:18px;line-height:32.4px;color:#222}
.sidebar li.current{color:var(--green);font-weight:500}
.ad-label{position:absolute;left:31px;top:1417px;font-size:9px;color:var(--muted)}
.ad-box{position:absolute;left:31px;top:1435px;width:300px;height:248px;background:var(--green-dark);color:#fff;text-align:center}
.ad-box h3{margin-top:80px;font-size:31px;font-weight:700;line-height:41px}
.ad-box p{font-size:13px;margin-top:12px}

/* profile */
.profile-title{position:absolute;left:360px;top:202px;font-size:27px;font-weight:500;color:var(--ink)}
.stars{position:absolute;left:734px;top:207px;display:flex;gap:3px}
.stars svg{width:22px;height:22px}
.badges{position:absolute;left:924px;top:200px;display:flex;gap:14px;align-items:center}
.badges span{display:block;width:46px;height:42px;background:var(--green)}
.badges span.round{border-radius:50%;background:#fff;border:4px solid var(--green)}
.badges span.yellow{background:#f2c31a;height:34px;width:54px}
.tabs{position:absolute;left:354px;top:263px;width:831px;height:34px;border-bottom:2px solid var(--line);font-size:15px;color:var(--muted)}
.tabs span{position:absolute;top:3px;transform:translateX(-50%)}
.tabs .active{color:var(--ink);font-weight:700;padding:0 18px 9px;border-bottom:3px solid var(--green)}

.slider{position:absolute;left:354px;top:320px;width:831px;height:470px}
.slide-side{position:absolute;top:0;width:96px;height:470px;background:linear-gradient(180deg,#d9e7c7,#b9c9a6 60%,#cfd8c2)}
.slide-main{position:absolute;left:103px;top:0;width:627px;height:470px;background:linear-gradient(180deg,#9fc2e8 0%,#7ea6c8 22%,#5b7d7f 38%,#4e7a3c 60%,#3e6a2a 100%)}
.slider .arrow{position:absolute;top:195px;width:24px;height:60px}

.section-title{position:absolute;left:358px;top:812px;font-size:27px;font-weight:400;color:var(--ink)}
.section-rule{position:absolute;left:358px;top:850px;width:827px;height:2px;background:var(--green)}
.desc{position:absolute;left:360px;top:866px;width:808px;font-size:14.5px;line-height:21.8px;color:#222}
.desc h4{font-size:17.5px;font-weight:500;color:var(--ink);line-height:24px}
.desc p{margin-bottom:21.8px}
.desc p.tight{margin-bottom:0}
.desc .block{margin-bottom:26px}

.info-head{position:absolute;left:360px;width:811px;font-size:17.5px;font-weight:500;color:var(--ink);border-bottom:2px solid var(--green);padding-bottom:6px}
.rows{position:absolute;left:360px;font-size:15px;color:#222}
.rows div{position:absolute;white-space:nowrap}

.feature{position:absolute;display:flex;align-items:center;font-size:15px;color:#222}
.feature svg{width:22px;height:18px;margin-right:18px}
.pay{position:absolute;display:flex;align-items:center;font-size:15px;color:#222}
.pay i{display:block;width:38px;height:38px;border-radius:50%;margin-right:10px}

/* footer */
.site-footer{position:absolute;left:0;top:2861px;width:1200px;height:621px;background:var(--footer)}
.site-footer h2{position:absolute;font-size:27px;font-weight:400;color:var(--ink)}
.about-text{position:absolute;left:35px;top:95px;width:375px;font-size:17.5px;line-height:22.4px;color:#222}
.link-col{position:absolute;top:87px;list-style:none;font-size:18px;line-height:36.9px;color:#222}
.footer-rule{position:absolute;left:38px;top:464px;width:1119px;height:1px;background:#bdbdbd}
.site-footer .brand{left:364px;top:512px;font-size:26px}
.social{position:absolute;left:534px;top:506px;display:flex;gap:17px}
.social span{display:block;width:49px;height:49px;border-radius:50%;background:var(--navy);border:3px solid #fff;box-shadow:0 0 0 2px var(--navy)}
.legal{position:absolute;left:0;top:581px;width:1200px;text-align:center;font-size:17.5px;color:#222}
</style>
</head>
<body>

<header class="site-header">
  <div class="brand"><span class="mark"></span>zeltfuchs</div>
  <div class="nav-item active" style="left:369px">
    <svg viewBox="0 0 30 30"><path d="M3 15 L15 4 L27 15 L24 15 L24 26 L18 26 L18 19 L12 19 L12 26 L6 26 L6 15 Z" fill="currentColor"/></svg>Home</div>
  <div class="nav-item" style="left:536px">
    <svg viewBox="0 0 30 30"><path d="M15 5 L27 27 L3 27 Z M10 2 L15 7 M20 2 L15 7" fill="#111" stroke="#111" stroke-width="2"/><path d="M15 16 L19 27 L11 27 Z" fill="#fff"/></svg>Campingplätze</div>
  <div class="nav-item" style="left:732px">
    <svg viewBox="0 0 30 30"><ellipse cx="15" cy="13" rx="13" ry="10" fill="#111"/><path d="M6 20 L4 28 L13 22 Z" fill="#111"/><circle cx="10" cy="13" r="1.8" fill="#fff"/><circle cx="15" cy="13" r="1.8" fill="#fff"/><circle cx="20" cy="13" r="1.8" fill="#fff"/></svg>Campingblog</div>
  <div class="nav-item" style="left:943px">
    <svg viewBox="0 0 30 30"><rect x="2" y="6" width="26" height="16" rx="3" fill="#111"/><rect x="6" y="10" width="6" height="5" fill="#fff"/><rect x="15" y="10" width="9" height="5" fill="#fff"/><circle cx="10" cy="23" r="3.5" fill="#111" stroke="#fff" stroke-width="1.5"/></svg>Was ist zeltfuchs?</div>
  <div class="nav-item" style="left:1125px">
    <svg viewBox="0 0 30 30"><circle cx="15" cy="10" r="5.5" fill="#111"/><path d="M5 27 C5 18 25 18 25 27 Z" fill="#111"/></svg>Anmelden</div>
</header>

<section class="search-band">
  <div class="search-field">
    <svg viewBox="0 0 24 34"><path d="M12 1 C5 1 1 6 1 12 C1 20 12 33 12 33 C12 33 23 20 23 12 C23 6 19 1 12 1 Z" fill="var(--green)"/><circle cx="12" cy="12" r="4" fill="#fff"/></svg>
    Nordsee
  </div>
  <div class="search-btn">Suchen</div>
</section>

<aside class="sidebar">
  <div class="title">Campingplätze</div>
  <div class="group" style="top:55px">Deutschland</div>
  <ul style="left:14px;top:88px">
    <li>Baden-Wüttenberg</li><li>Bayern</li><li>Berlin</li><li>Bremen</li><li>Hamburg</li><li>Hessen</li><li>Mecklenburg-Vorpommern</li><li class="current">Niedersachsen</li>
  </ul>
  <ul style="left:29px;top:350px">
    <li>Wesermarsch</li><li>Harz</li><li>Norddeich</li><li>Oberharz</li><li>Otterndorf</li><li>Hannover</li><li>Nordseeküste</li><li class="current">Lüneburger Heide</li><li>Wangerland</li><li>Weserbergland</li><li>Hameln</li><li>Harz</li><li>Unterelbe</li><li>Wendland</li><li>Wilhelmshaven</li>
  </ul>
  <div class="group" style="top:855px">Österreich</div>
  <div class="group" style="top:909px">Schweiz</div>
  <div class="group" style="top:965px">Italien</div>
  <div class="group" style="top:1019px">Frankreich</div>
  <div class="group" style="top:1074px">Niederlande</div>
  <div class="group" style="top:1129px">Belgien</div>
</aside>
<div class="ad-label">Anzeige</div>
<div class="ad-box"><h3>Größe eines<br>Rectangle Banners</h3><p>(300 x 250 Pixel)</p></div>

<h1 class="profile-title">Campingplatz Elbauen Strand</h1>
<div class="stars">
  <svg viewBox="0 0 24 24"><path d="M12 1 L15 9 L23 9 L17 14 L19 22 L12 17 L5 22 L7 14 L1 9 L9 9 Z" fill="var(--green)"/></svg>
  <svg viewBox="0 0 24 24"><path d="M12 1 L15 9 L23 9 L17 14 L19 22 L12 17 L5 22 L7 14 L1 9 L9 9 Z" fill="var(--green)"/></svg>
  <svg viewBox="0 0 24 24"><path d="M12 1 L15 9 L23 9 L17 14 L19 22 L12 17 L5 22 L7 14 L1 9 L9 9 Z" fill="var(--green)"/></svg>
  <svg viewBox="0 0 24 24"><path d="M12 1 L15 9 L23 9 L17 14 L19 22 L12 17 L5 22 L7 14 L1 9 L9 9 Z" fill="var(--green)"/></svg>
</div>
<div class="badges">
  <span class="round" role="img" aria-label="Prüfsiegel"></span>
  <span role="img" aria-label="Clubsiegel"></span>
  <span class="round" style="border-color:#4aa3df" role="img" aria-label="Umweltsiegel"></span>
  <span class="yellow" role="img" aria-label="Kartenpartner"></span>
</div>
<nav class="tabs">
  <span class="active" style="left:40px">Profil</span>
  <span style="left:128px">Lage</span>
  <span style="left:243px">Ausstattung</span>
  <span style="left:361px">Freizeit</span>
  <span style="left:500px">Mietunterkunft</span>
  <span style="left:644px">Bewertung</span>
  <span style="left:768px">Kontakt</span>
</nav>

<div class="slider">
  <div class="slide-side" style="left:0" role="img" aria-label="Vorheriges Bild: Stellplätze im Grünen"></div>
  <div class="slide-main" role="img" aria-label="Luftaufnahme des Campingplatzes am Elbufer mit Stellplätzen, Deich und Yachthafen"></div>
  <div class="slide-side" style="left:735px" role="img" aria-label="Nächstes Bild: Stellplätze im Grünen"></div>
  <svg class="arrow" style="left:6px" viewBox="0 0 24 60"><path d="M20 4 L6 30 L20 56" stroke="var(--navy)" stroke-width="6" fill="none"/></svg>
  <svg class="arrow" style="left:800px" viewBox="0 0 24 60"><path d="M4 4 L18 30 L4 56" stroke="var(--navy)" stroke-width="6" fill="none"/></svg>
</div>

<h2 class="section-title">Campingplatz Beschreibung</h2>
<div class="section-rule"></div>
<div class="desc">
  <div class="block">
    <h4>Campingplatz Elbauen Strand - in der Nähe von Hamburg</h4>
    <p>Der Campingplatz Elbauen Strand befindet sich in Drage am Elbstrand der Elbe in der Nähe der Weltstadt Hamburg. Der Platz ist ganzjährig geöffnet. Auf dem Gelände befinden sich ein ebenfalls ganzjährig geöffneter Frischkauf-Markt und eine Gastwirtschaft.</p>
    <p class="tight">Die Lage vom Campingplatz Elbauen Strand an der Elbe ermöglicht ein abwechslungsreiches Freizeitprogramm: Sie können in der Parkanlage spazieren gehen, Sie können am Strand sitzen, angeln oder baden. Sie können aber auch ein Fahrrad leihen und in der Marschlandschaft, an der Elbe radeln.<br>Campingplatz Elbauen Strand - die Ausstattung</p>
    <p style="margin-top:21.8px">In dem erneuerten Badehaus vom Campingplatz Elbauen Strand sind sowohl große Waschräume als auch Einzelkabinen. Umkleide- und Toilettenhäuser werden zur Saison aufgestellt. Sie sind komfortabel ausgestattet. Koch- und Abwaschbereich sind im gleichen Gebäude untergebracht wie die Waschküche.<br>Der Campingplatz Elbauen Strand bietet zudem: Bootshafen, Fußball- und Basketballfelder, Grillplätze, Wasserski, Behindertenanlagen, Babywickelraum, Kinderspielplatz mit verschiedenen Spielgeräten, Fahrradverleih, Wohnmobilstellplätze direkt am Wasser incl. Entsorgung, Imbiss, Restaurant und SB-Laden. Außerdem in der Umgebung: Schwimmbad, Tennis, Reiten, Kegelbahn.</p>
    <p class="tight">Als Jahresplätze stehen 450 Plätze zu je 130 qm zur Verfügung. Es stehen zur Verfügung: modernste Sanitäranlagen, Strom- und Wasseranschluss, Kochküche, Münzwaschsalon mit Trockner, Gasverkauf.<br>Die auf dem Campingplatz Elbauen Strand vorhandenen Mietwohnwagen stehen als kostengünstige Unterkunft zur Verfügung. Sie sind mit 4 Schlafplätzen ausgestattet und haben ein großes Vorzelt mit Sitzgruppe. In den Mietwohnwagen darf nicht geraucht werden. Mietmobilheime sind ebenfalls für 4 Personen eingerichtet und haben eine Küchenzeile und ein Badezimmer. Rauchen ist nicht erlaubt, Tierhaltung nur teilweise. Ferienhäuser haben ein Wohnzimmer mit TV, 4 Schlafplätze, eine Küchenzeile und ein Badezimmer. Rauchen und Tierhaltung sind nicht erlaubt.<br>Beim Camping am Elbauen Strand bleiben keine Wünsche offen.</p>
  </div>
  <div class="block">
    <h4>Campingplatz Elbauen Strand - Kulinarisches</h4>
    <p class="tight">Auf dem Campingplatz Elbauen Strand befindet sich das gleichnamige Restaurant, das über 120 Sitzplätze verfügt, eine Terrasse und einen Wintergarten mit Kamin. Das Restaurant bietet neben den a la carte- Angeboten fast täglich wechselnde regionale Spezialitäten an.</p>
  </div>
  <div class="block">
    <h4>Campingplatz Elbauen Strand - Animation und Ausflüge</h4>
    <p class="tight">Von Mai bis Mitte September wird auf dem Campingplatz Elbauen Strand ein Animationsprogramm angeboten. Dazu kommen viele Feste.<br>Ausflugsziele sind u.a. Hamburg, Lauenburg, Lüneburg, Winsen, Geesthacht.<br>Vom Fahrgastschiffanleger im eigenen Yachthafen werden Fahrten nach Hamburg mit dem größten Hafen Deutschlands und den vielen Sehenswürdigkeiten angeboten.</p>
  </div>
</div>

<div class="info-head" style="top:1757px">Öffnungszeiten</div>
<div class="rows" style="top:0">
  <div style="top:1826px;left:0">Jährlich geöffnet</div><div style="top:1826px;left:405px">01.01 - 31.12</div>
  <div style="top:1872px;left:0">Check-In Zeiten</div><div style="top:1872px;left:383px">08:00 - 20:00 Uhr</div>
  <div style="top:1918px;left:0">Mittagspause</div><div style="top:1918px;left:383px">13:00 - 15:00 Uhr</div>
</div>

<div class="info-head" style="top:2001px">Anzahl der Stellplätze</div>
<div class="rows" style="top:0">
  <div style="top:2048px;left:0">Stellplätze [Gesamt]</div><div style="top:2048px;left:451px">500</div>
  <div style="top:2094px;left:0">Fest gebucht</div><div style="top:2094px;left:451px">400</div>
  <div style="top:2140px;left:0">Frei belegbar</div><div style="top:2140px;left:451px">100</div>
  <div style="top:2185px;left:0">Stellplätze ohne Stromanschluss</div><div style="top:2185px;left:451px">k. A.</div>
  <div style="top:2231px;left:0">Stellplätze mit Stromanschluss</div><div style="top:2231px;left:451px">100</div>
  <div style="top:2276px;left:0">Stellplätze mit Schattendächern</div><div style="top:2276px;left:451px">k. A.</div>
  <div style="top:2322px;left:0">Stellplätze mit Frisch-/Abwasseranschluss</div><div style="top:2322px;left:451px">100</div>
</div>

<div class="info-head" style="top:2387px">Besonderheiten</div>
<div class="feature" style="left:365px;top:2441px"><svg viewBox="0 0 22 18"><path d="M2 9 L8 15 L20 2" stroke="var(--green)" stroke-width="4" fill="none"/></svg>Direkt am Wasser</div>
<div class="feature" style="left:365px;top:2487px"><svg viewBox="0 0 22 18"><path d="M2 9 L8 15 L20 2" stroke="var(--green)" stroke-width="4" fill="none"/></svg>Haustier erlaubt (Hunde,Katzen, etc.)</div>
<div class="feature" style="left:365px;top:2532px"><svg viewBox="0 0 22 18"><path d="M2 9 L8 15 L20 2" stroke="var(--green)" stroke-width="4" fill="none"/></svg>KCV Campingplatz</div>
<div class="feature" style="left:365px;top:2578px"><svg viewBox="0 0 22 18"><path d="M2 9 L8 15 L20 2" stroke="var(--green)" stroke-width="4" fill="none"/></svg>Naturbelassener Campingplatz</div>
<div class="feature" style="left:749px;top:2441px"><svg viewBox="0 0 22 18"><path d="M2 9 L8 15 L20 2" stroke="var(--green)" stroke-width="4" fill="none"/></svg>Eco Camping</div>
<div class="feature" style="left:749px;top:2487px"><svg viewBox="0 0 22 18"><path d="M2 9 L8 15 L20 2" stroke="var(--green)" stroke-width="4" fill="none"/></svg>Offenes Feuer erlaubt</div>
<div class="feature" style="left:749px;top:2532px"><svg viewBox="0 0 22 18"><path d="M2 9 L8 15 L20 2" stroke="var(--green)" stroke-width="4" fill="none"/></svg>zeltfuchs Geprüft</div>
<div class="feature" style="left:749px;top:2578px"><svg viewBox="0 0 22 18"><path d="M2 9 L8 15 L20 2" stroke="var(--green)" stroke-width="4" fill="none"/></svg>PlatzKarte</div>

<div class="info-head" style="top:2649px">Zahlungsmöglichkeiten</div>
<div class="pay" style="left:359px;top:2695px"><i style="background:#1e3f8a"></i>Kartenwerk</div>
<div class="pay" style="left:580px;top:2695px"><i style="background:#35a9e0"></i>Globalpay Express</div>
<div class="pay" style="left:827px;top:2695px"><i style="background:#3a72b8"></i>Mondkarte</div>
<div class="pay" style="left:359px;top:2752px"><i style="background:#1b3f8c"></i>EC-/Tresor Card</div>
<div class="pay" style="left:580px;top:2752px"><i style="background:#3f9fd0"></i>Barzahlung</div>

<footer class="site-footer">
  <h2 style="left:35px;top:28px">Warum zeltfuchs?</h2>
  <p class="about-text">Lorem ipsum dolor sit amet, consetetur sadipscing elitr, sed diam nonumy eirmod tempor invidunt ut labore et dolore magna aliquyam erat, sed diam voluptua. At vero eos et accusam et justo duo dolores et ea rebum. Stet clita kasd gubergren, no sea takimata sanctus est Lorem ipsum dolor sit amet. Lorem ipsum dolor sit amet, consetetur sadipscing elitr, sed diam nonumy eirmod tempor invidunt ut labore et dolore magna aliquyam erat, sed diam voluptua. At vero eos et accusam et justo duo dolores et ea rebum. Stet clita kasd gubergren, no sea takimata sanctus est</p>

  <h2 style="left:522px;top:26px">Top Regionen</h2>
  <ul class="link-col" style="left:523px"><li>Allgäu</li><li>Südtirol</li><li>Mallorca</li><li>Tirol</li><li>Oberstdorf</li><li>Fuerteventura</li><li>Sardinien</li><li>Schwarzwald</li><li>Schweiz</li></ul>
  <ul class="link-col" style="left:697px"><li>Bayerischen</li><li>Wald</li><li>Teneriffa</li><li>Harz</li><li>Gran Canaria</li><li>Bayerischen</li><li>Wald</li><li>Teneriffa</li><li>Harz</li></ul>

  <h2 style="left:897px;top:26px">Top Städte</h2>
  <ul class="link-col" style="left:901px"><li>Berlin</li><li>Rostock</li><li>Frankfurt</li><li>Köln</li><li>Paris</li><li>St. Tropez</li><li>München</li><li>Toulouse</li><li>Rom</li></ul>
  <ul class="link-col" style="left:1048px"><li>Berlin</li><li>Rostock</li><li>Frankfurt</li><li>Köln</li><li>Paris</li><li>St. Tropez</li><li>München</li><li>Toulouse</li><li>Rom</li></ul>

  <div class="footer-rule"></div>
  <div class="brand"><span class="mark"></span>zeltfuchs</div>
  <div class="social">
    <span role="img" aria-label="Soziales Netzwerk 1"></span>
    <span role="img" aria-label="Soziales Netzwerk 2"></span>
    <span role="img" aria-label="Soziales Netzwerk 3"></span>
    <span role="img" aria-label="Videoportal"></span>
    <span role="img" aria-label="E-Mail"></span>
  </div>
  <div class="legal">Campingplatz anmelden &nbsp;|&nbsp; Sitemap &nbsp;|&nbsp; Kontakt &nbsp;|&nbsp; Impressum &nbsp;|&nbsp; &nbsp;© 2013-2015 zeltfuchs</div>
</footer>

</body>
</html>
```